An our door sign really promoting our clinic and services

We have a new sports medicine clinic called HALLCREST SPORTS MEDICINE.
We want to make a really nice external sign at our clinic using a photo of our team we really like. I have attached the photo.
We want to simply include our LOGO and also signs with these slogan options. So we want different signs with these different slogans so we can choose what we really like.
This should be a simple and quite design.

The SLOGANS WE WOULD LIKE TO SEE ON THE SIGN (only one slogan per sign in the drafts)

1. Your Journey. Our Expertise
2. Where better health begins
3. Building the best version of you
4. Your health, in expert hands
5. Reaching new heights in your health
6. Your path to peak performance starts here

I have also included different versions of our logo based on the background and how you set the sign up

So summary
1. Image attached
2. Slogan options we would like to see them all
3. Logo attached (various options based on how you set the background up)
4. Size of sign is 2935mm wide x 1885mm high

```html
<!DOCTYPE html>
<html lang="en">
<head>
<meta charset="utf-8">
<title>Hallcrest Sports Medicine – Where Better Health Begins</title>
<link rel="stylesheet" href="https://fonts.googleapis.com/css2?family=Barlow+Condensed:ital,wght@1,800;1,900&family=Saira:wght@700&display=swap">
<style>
  :root {
    --navy: #161c4b;
    --sky: #4fc3e8;
    --white: #ffffff;
    --gym-light: #f3f3f2;
    --gym-mid: #d6d3ce;
    --gym-warm: #b9b2a8;
    --team-dark: #2b2f45;
    --team-shade: #474a5c;
  }
  * { margin: 0; padding: 0; box-sizing: border-box; }
  html, body { width: 1200px; height: 797px; overflow: hidden; background: var(--white); }
  .sign {
    position: relative;
    width: 1200px;
    height: 797px;
    overflow: hidden;
  }
  .gym-backdrop {
    position: absolute;
    inset: 0;
    background: linear-gradient(115deg, var(--gym-light) 0%, var(--gym-light) 28%, var(--gym-mid) 55%, var(--gym-warm) 100%);
  }
  .team-photo {
    position: absolute;
    left: 585px;
    top: 160px;
    width: 590px;
    height: 637px;
    border-radius: 180px 180px 0 0;
    background:
      radial-gradient(ellipse 60% 55% at 50% 65%, var(--team-dark) 0%, rgba(43,47,69,0.85) 45%, rgba(71,74,92,0) 100%),
      linear-gradient(180deg, rgba(71,74,92,0) 0%, rgba(71,74,92,0.55) 35%, rgba(43,47,69,0.8) 100%);
  }
  .shapes {
    position: absolute;
    inset: 0;
    width: 1200px;
    height: 797px;
  }
  .brand {
    position: absolute;
    left: 852px;
    top: 62px;
    display: flex;
    align-items: center;
    gap: 14px;
  }
  .brand-dot {
    width: 20px;
    height: 20px;
    border-radius: 50%;
    background: var(--sky);
  }
  .brand-name {
    font-family: "Saira", sans-serif;
    font-weight: 700;
    color: var(--white);
    line-height: 1;
  }
  .brand-name .primary { display: block; font-size: 35px; letter-spacing: 6px; }
  .brand-name .secondary { display: block; font-size: 13px; letter-spacing: 9.6px; margin-top: 7px; }
  .headline {
    font-family: "Barlow Condensed", sans-serif;
    font-style: italic;
    font-weight: 900;
    text-transform: uppercase;
    line-height: 1;
    position: absolute;
    white-space: nowrap;
  }
  .headline-where { left: 100px; top: 253px; font-size: 74px; color: var(--navy); letter-spacing: 2px; }
  .headline-better { left: 62px; top: 309px; font-size: 148px; color: var(--navy); letter-spacing: 0; }
  .headline-health { left: 78px; top: 431px; font-size: 148px; color: var(--white); letter-spacing: 6px; }
  .begins-box {
    position: absolute;
    left: 265px;
    top: 582px;
    width: 274px;
    height: 108px;
    background: var(--navy);
  }
  .headline-begins { left: 296px; top: 596px; font-size: 80px; color: var(--white); letter-spacing: 3px; }
</style>
</head>
<body>
<main class="sign">
  <div class="gym-backdrop"></div>
  <div class="team-photo" role="img" aria-label="Team photo: a clinician in a navy polo shows a tablet to a smiling athlete in a black t-shirt, in a softly blurred gym setting"></div>

  <svg class="shapes" viewBox="0 0 1200 797" aria-hidden="true">
    <path class="sky-panel" fill="var(--sky)" d="M0 131 C 330 150, 600 430, 658 797 L0 797 Z"/>
    <path class="navy-panel" fill="var(--navy)" d="M495 0 L1200 0 L1200 274 C 1100 278, 1000 272, 935 236 C 810 165, 700 45, 495 0 Z"/>
  </svg>

  <div class="brand">
    <span class="brand-dot"></span>
    <p class="brand-name"><span class="primary">HALLCREST</span><span class="secondary">SPORTS MEDICINE</span></p>
  </div>

  <h1>
    <span class="headline headline-where">Where</span>
    <span class="headline headline-better">Better</span>
    <span class="headline headline-health">Health</span>
    <span class="begins-box"></span>
    <span class="headline headline-begins">Begins</span>
  </h1>
</main>
</body>
</html>
```